Red Kettle Handcrafted Tomato Ketchup packaging design modern

From the best ingredients there is the best ketchup Red Handcrafted ketchup are specially formulated for fine dining and drinks, bringing out all the flavors. As the Red Kettle handcrafted ketchup is otherwise fabulous: Made with wholesome, fully ripe fruits Nothing with half things! All Red Kettle handcrafted ketchups are pure nature, without any artificial diluents or concentrates. Where tomato is on it, that's all there is to it - guaranteed! the design should be professional and noble despite being trendy. A watcher wants to sell the ketchup as merchandising from our restaurant. but as a single brand positioning. The ketchup is vegan. Dimensions: 6.8 cm Height: 7.8 cm Circumference: 21.6 cm The text down (Text 1-4). The lid of the text the glass packaging is black! Thanks for your efforts. I look forward to your designs.

Target Market(s)

foodies

Font styles to use
Serif
Sans Serif

Colors

Designer to choose colors to be used in the design.

Requirements
Must have
• Title: (Handcrafted Tomato Ketchup) Text One: (Store chilled after opening and consume quickly, pasteurized.) Text Two: (Handcrafted in Switzerland by Brentwick Gastro GmbH, Chur www.redkettle-example.ch) Text Tree: (Tomatoes, White Wine Vinegar, Aceto Balsamico, Brown Cane Sugar, Corn Starch, Spices, Salt) Text For: (200 grams) or (200g) The Logo of Red Kettle with the Pasta and Wine have to because of the gesety.
Nice to have
• small vegan icon (maybe)
Should not have
• text of the logo (pasta & wine)

```html
<!DOCTYPE html>
<html lang="en">
<head>
<meta charset="utf-8">
<title>Red Kettle – Tomato Ketchup Label</title>
<link rel="stylesheet" href="https://fonts.googleapis.com/css2?family=Montserrat:wght@500&family=Staatliches&family=Courier+Prime:wght@700&display=swap">
<style>
  :root {
    --page-bg: #f2efec;
    --label-black: #141212;
    --label-white: #f4f1ec;
    --tomato-red: #d8323a;
    --tomato-deep: #a81f27;
  }
  * { margin: 0; padding: 0; box-sizing: border-box; }
  html, body {
    width: 952px;
    height: 1200px;
    overflow: hidden;
    background: var(--page-bg);
  }
  .canvas {
    position: relative;
    width: 952px;
    height: 1200px;
  }
  .label {
    position: absolute;
    left: 46px;
    top: 305px;
    width: 860px;
    height: 590px;
    background: var(--label-black);
    color: var(--label-white);
  }
  .brand-name {
    position: absolute;
    top: 90px;
    left: 0;
    width: 100%;
    text-align: center;
    font-family: "Montserrat", sans-serif;
    font-weight: 500;
    font-size: 34px;
    letter-spacing: 0.14em;
  }
  .tomato-artwork {
    position: absolute;
    left: 240px;
    top: 165px;
    width: 380px;
    height: 170px;
    border-radius: 190px 190px 12px 12px;
    background: radial-gradient(ellipse at 50% 70%, var(--tomato-red) 0%, var(--tomato-deep) 38%, rgba(20,18,18,0) 72%);
  }
  .product-title {
    position: absolute;
    top: 340px;
    left: 0;
    width: 100%;
    text-align: center;
    font-family: "Staatliches", sans-serif;
    font-size: 98px;
    line-height: 1;
    letter-spacing: 0.01em;
  }
  .product-tag {
    position: absolute;
    top: 458px;
    left: 0;
    width: 100%;
    display: flex;
    align-items: center;
    justify-content: center;
    gap: 22px;
  }
  .product-tag .rule {
    display: block;
    width: 120px;
    height: 3px;
    background: var(--label-white);
  }
  .product-tag .tag-text {
    font-family: "Courier Prime", monospace;
    font-weight: 700;
    font-size: 32px;
    letter-spacing: 0.12em;
  }
</style>
</head>
<body>
  <main class="canvas">
    <section class="label">
      <p class="brand-name">RED KETTLE</p>
      <div class="tomato-artwork" role="img" aria-label="Illustration of two red tomatoes with white sun rays radiating behind them"></div>
      <h1 class="product-title">TOMATO KETCHUP</h1>
      <div class="product-tag">
        <span class="rule"></span>
        <span class="tag-text">HANDCRAFTED</span>
        <span class="rule"></span>
      </div>
    </section>
  </main>
</body>
</html>
```